Full Website and E-Commerce Design. New Business. Selling digital downloads related to the call cen

I am planning to launch a new online company called maplequartzservices.com. This will be a place where people who work in call centres can come and purchase downloadable templates, tool-kits, courseware etc to help them in their jobs. The site will also share the latest information around research, best practices, news in the industry. Essentially a hub for everything call centre related.

I need someone to build the site for me from scratch (I have only just bought the domain name). Everything from the look and feel of the website (focus on easy to use, clean and sharp graphics, with a bit of fun), highly focused on social media and building a community, full blown e-commerce that allows for memberships/subscriptions/and one off purchase models. If you can also design custom graphics (high quality) that would be even better. Given my research of other companies in this space their websites are very dull that look like knowledge bases. I will want alot of cool visuals that attract the customers in. My initial thinking on colour scheme is bright greens/pinks/yellows etc. Not fluorescent though!

The site will contain alot of documents, templates, presentations, videos, articles, white papers etc. You must have experience in the best way to structure the site in an organised manner so that my customer can find what they need very easily.

The person who takes on this work must be happy to work collaboratively with me. It is also key that when the project is delivered that I am able to maintain alot of it myself in terms of uploading documents, blog updates, adding new products, real-time reports/analytics etc.

Whilst you are designing the website I will be working on the content so I will need your help to understand how I structure my content so that it makes sense for the design.

I will base my choice of designer on levels of experience (I will want to see previous work that you have done). I am not adverse to you using tools like shopify etc. if it meets the overall requirements of the site and adds to the functionality/look and feel.

Target Market(s)

People who work in call centres primarily those that are responsible for managing teams of the call centre itself

Industry/Entity Type

Business

Number of Pages Required

5+ page

Font styles to use
Sans Serif

Colors
33b8a4
34a6d7
886aae
b868aa
e667a6
f04a51
f68e4e
faa54b
ffcf3e

Requirements
Must have
• E-commerce functionality that allows for subscriptions and one-off payments
• Credit card processing and accept wire/bank transfers
• Easy to use layout
• Products sold alone and/or as part of bundles
• Membership area
• Front page
• About Us page
• Contact Us page
• Store page (with e-commerce back end)
• News page
• Free Resources page
• Cool, bright, fun look and feel
Nice to have
• Cool, bright, fun graphics
Should not have
• Should not look old fashioned or be difficult to navigate
• Should not look too busy or disorganised

```html
<!DOCTYPE html>
<html lang="en">
<head>
<meta charset="utf-8">
<title>Maple Quartz Services – Home</title>
<link rel="stylesheet" href="https://fonts.googleapis.com/css2?family=Source+Sans+3:wght@400;600;700&display=swap">
<style>
:root{
  --teal:#33b8a4;
  --blue:#34a6d7;
  --violet:#886aae;
  --orchid:#b868aa;
  --pink:#e667a6;
  --red:#f04a51;
  --orange:#f68e4e;
  --amber:#faa54b;
  --yellow:#ffcf3e;
  --nav:#12b6f1;
  --nav-active:#5fd3f8;
  --nav-text:#1b3a50;
  --plum:#8e5a8c;
  --ink:#2b2b2b;
  --white:#ffffff;
}
*{box-sizing:border-box;margin:0;padding:0}
html,body{width:1200px;height:769px;overflow:hidden}
body{font-family:"Source Sans 3",sans-serif;color:var(--ink);background:#fff;position:relative}

.site-header{position:absolute;left:0;top:0;width:1200px;height:98px;
  background:linear-gradient(90deg,#ffffff 0%,#f4f5f6 40%,#e9ecee 75%,#dfe3e6 100%)}
.brand{position:absolute;left:243px;top:18px;display:flex;align-items:center;gap:10px}
.brand-dot{width:52px;height:52px;border-radius:50%;background:var(--ink)}
.brand-name{font-weight:700;font-size:24px;line-height:25px;color:#1a9fe3;letter-spacing:.5px;text-transform:uppercase}
.contact-line{position:absolute;left:716px;top:16px;font-size:11px;color:#333;display:flex;gap:14px;align-items:center}
.contact-line span{display:flex;align-items:center;gap:4px}
.secondary-links{position:absolute;left:606px;top:45px;font-size:12px;letter-spacing:.6px;line-height:20px;color:#333}
.cart{position:absolute;left:737px;top:55px}
.divider{position:absolute;left:770px;top:47px;width:1px;height:29px;background:#d3d6d8}
.login{position:absolute;left:788px;top:54px;font-size:13.5px;letter-spacing:.3px;color:#111}
.register{position:absolute;left:840px;top:47px;width:124px;height:29px;background:var(--plum);
  color:#fff;font-size:13px;display:flex;align-items:center;justify-content:center;gap:22px;border-radius:2px}

.main-nav{position:absolute;left:0;top:98px;width:1200px;height:55px;background:var(--nav);border-bottom:2px solid #6fd3f6}
.main-nav a{position:absolute;top:0;height:53px;display:flex;align-items:center;font-size:14.5px;letter-spacing:.8px;color:var(--nav-text);text-decoration:none}
.main-nav a.active{background:var(--nav-active);justify-content:center}
.main-nav .sep{position:absolute;top:15px;width:1px;height:23px;background:rgba(0,0,0,.08)}
.search{position:absolute;left:805px;top:115px;width:165px;height:24px;background:#fff;border-radius:12px;
  font-size:10px;font-style:italic;color:#777;padding:6px 0 0 7px}
.search svg{position:absolute;right:7px;top:6px}

.hero{position:absolute;left:0;top:153px;width:1200px;height:545px;
  background:radial-gradient(ellipse at 50% 40%,#8d8d8f 0%,#6f7072 55%,#535456 100%)}
.tile{position:absolute;width:217px;height:137px;display:flex;align-items:center;justify-content:center;
  text-align:center;color:#fff;font-size:18.5px;line-height:21.5px;text-transform:uppercase;padding-top:38px;
  box-shadow:0 1px 3px rgba(0,0,0,.25)}
.tile.dark{color:#1f2a33}

.site-footer{position:absolute;left:0;top:698px;width:1200px;height:71px;background:var(--plum);color:#fff;font-size:10px}
.legal{position:absolute;left:235px;top:31px;display:flex;gap:7px}
.legal b{font-weight:600}
.payments{position:absolute;left:593px;top:27px;display:flex;align-items:center;gap:10px}
.payments .label{font-weight:600}
.card{width:30px;height:18px;border-radius:2px;background:#f3f3f3}
.card.dark{background:#1e1e1e}
.card.warm{background:#f6e6b4}
.social{position:absolute;left:885px;top:28px;display:flex;gap:5px}
.social span{width:16px;height:16px;border:1px solid rgba(255,255,255,.7);border-radius:50%}
</style>
</head>
<body>

<header class="site-header">
  <div class="brand"><div class="brand-dot"></div><div class="brand-name">Maple Quartz<br>Services</div></div>
  <div class="contact-line">
    <span><svg width="9" height="9" viewBox="0 0 10 10"><path d="M2 1l2 2-1 1.3c.6 1.3 1.4 2.1 2.7 2.7L7 6l2 2-1.3 1.3C4.5 9 1 5.5.7 2.3z" fill="#444"/></svg>555-018-2044</span>
    <span><svg width="10" height="8" viewBox="0 0 10 8"><rect width="10" height="8" rx="1" fill="#555"/><path d="M0 1l5 3.5L10 1" stroke="#fff" fill="none"/></svg>info@maplequartzservices.com</span>
  </div>
  <nav class="secondary-links"><div>ABOUT US</div><div>FREE RESOURCES</div></nav>
  <svg class="cart" width="15" height="13" viewBox="0 0 15 13"><path d="M1 1h2l2 7h7l1.5-5H4" fill="none" stroke="#222" stroke-width="1.4"/><circle cx="6" cy="11" r="1.2" fill="#222"/><circle cx="11" cy="11" r="1.2" fill="#222"/></svg>
  <div class="divider"></div>
  <div class="login">LOGIN</div>
  <a class="register">REGISTER <svg width="7" height="10" viewBox="0 0 7 10"><path d="M1 1l4 4-4 4" stroke="#fff" stroke-width="1.6" fill="none"/></svg></a>
</header>

<nav class="main-nav">
  <a class="active" style="left:230px;width:77px">HOME</a>
  <a style="left:322px">NEWS</a>
  <span class="sep" style="left:377px"></span>
  <a style="left:392px">FREE STUFF</a>
  <span class="sep" style="left:486px"></span>
  <a style="left:502px">MEMBERSHIP</a>
  <span class="sep" style="left:607px"></span>
  <a style="left:621px">CONTACT US</a>
</nav>
<div class="search">Search<svg width="11" height="11" viewBox="0 0 11 11"><circle cx="4.5" cy="4.5" r="3.5" stroke="#555" stroke-width="1.3" fill="none"/><path d="M7 7l3 3" stroke="#555" stroke-width="1.4"/></svg></div>

<main class="hero" role="img" aria-label="Photo of smiling call centre agents wearing headsets at their desks">
  <div class="tile" style="left:253px;top:37px;background:rgba(51,184,164,.88);padding-top:20px">Performance<br>Measurement &amp;<br>Management</div>
  <div class="tile dark" style="left:496px;top:37px;background:rgba(52,166,215,.85)">Moral &amp;<br>Motivation</div>
  <div class="tile" style="left:740px;top:37px;background:rgba(136,106,174,.88);padding-top:34px">Coaching<br>&amp; Mentoring</div>
  <div class="tile" style="left:253px;top:199px;background:rgba(184,104,170,.88)">Leadership<br>&amp; Management</div>
  <div class="tile" style="left:496px;top:199px;background:rgba(230,103,166,.88)">Reward<br>&amp; Recognition</div>
  <div class="tile" style="left:740px;top:199px;background:rgba(240,74,81,.85);padding-top:42px">Communication<br>Skills</div>
  <div class="tile" style="left:253px;top:360px;background:rgba(246,142,78,.9);padding-top:42px">Call Center<br>Technology</div>
  <div class="tile" style="left:496px;top:360px;background:rgba(250,165,75,.9);padding-top:42px">Call Center<br>Strategy</div>
  <div class="tile" style="left:740px;top:360px;background:rgba(255,207,62,.88);padding-top:44px">Research &amp;<br>Best Practices</div>
</main>

<footer class="site-footer">
  <div class="legal"><span>© 2015. <b>Maple Quartz Services</b></span><span>|</span><span>Privacy Policy</span><span>|</span><span>Terms &amp; Conditions</span></div>
  <div class="payments"><span class="label">We Accept :</span><span class="card"></span><span class="card"></span><span class="card dark"></span><span class="card warm"></span></div>
  <div class="social"><span></span><span></span><span></span><span></span></div>
</footer>

</body>
</html>
```